washable paper bags and accessories

We are three sisters who have discovered a mutual love of bags made from washable paper. It is a brand new business venture for bags, handbags, cosmetic bags, and home storage solutions and décor all made with washable paper.
We would like to have white crumpled paper as a background for both sides. Front of card with the words "plume douce cloth" only in "bohemian typewriter regular" font. Back of card with appointment style format for our next pop up stall
Target Market(s)
mums, females
Industry/Entity Type
Business
Contact Information for Business Card
ph: 0487215364
email:plumedoucecloth@mailbarrow.com

```html
<!DOCTYPE html>
<html lang="en">
<head>
<meta charset="utf-8">
<title>plume douce cloth – business card</title>
<link rel="stylesheet" href="https://fonts.googleapis.com/css2?family=Special+Elite&display=swap">
<style>
  :root {
    --canvas-bg: #ffffff;
    --paper-light: #fbfbfc;
    --paper-mid: #eeeef1;
    --paper-shadow: #dcdce1;
    --ink: #1c1c1c;
    --card-shadow: rgba(0, 0, 0, 0.32);
  }
  * { margin: 0; padding: 0; box-sizing: border-box; }
  html, body {
    width: 1200px;
    height: 960px;
    overflow: hidden;
    background: var(--canvas-bg);
  }
  .canvas {
    position: relative;
    width: 1200px;
    height: 960px;
    background: var(--canvas-bg);
  }
  .card {
    position: absolute;
    left: 290px;
    width: 620px;
    height: 384px;
    box-shadow: 0 4px 9px var(--card-shadow);
    overflow: hidden;
    font-family: "Special Elite", "Courier New", monospace;
    color: var(--ink);
  }
  .card--back { top: 60px; }
  .card--front { top: 516px; }
  .paper-texture {
    position: absolute;
    inset: 0;
    background:
      radial-gradient(ellipse at 22% 30%, var(--paper-light) 0%, transparent 55%),
      radial-gradient(ellipse at 75% 70%, var(--paper-light) 0%, transparent 50%),
      radial-gradient(ellipse at 60% 20%, var(--paper-shadow) 0%, transparent 45%),
      radial-gradient(ellipse at 30% 80%, var(--paper-shadow) 0%, transparent 45%),
      linear-gradient(135deg, var(--paper-mid), var(--paper-light) 50%, var(--paper-mid));
  }
  .card-content { position: relative; width: 100%; height: 100%; }
  .visit-heading {
    position: absolute;
    top: 66px;
    width: 100%;
    text-align: center;
    font-size: 24px;
    letter-spacing: 0.5px;
  }
  .brand-name {
    position: absolute;
    top: 70px;
    width: 100%;
    text-align: center;
    font-size: 42px;
    letter-spacing: 1px;
  }
  .contact-list {
    position: absolute;
    top: 26px;
    left: 28px;
    list-style: none;
    font-size: 12px;
    line-height: 1.5;
  }
</style>
</head>
<body>
<main class="canvas">
  <section class="card card--back" aria-label="Card back">
    <div class="paper-texture" role="img" aria-label="White crumpled paper texture"></div>
    <div class="card-content">
      <p class="visit-heading">come visit us at</p>
    </div>
  </section>

  <section class="card card--front" aria-label="Card front">
    <div class="paper-texture" role="img" aria-label="White crumpled paper texture"></div>
    <div class="card-content">
      <ul class="contact-list">
        <li>0487215364</li>
        <li>plumedoucecloth@mailbarrow.com</li>
      </ul>
      <h1 class="brand-name">plume douce cloth</h1>
    </div>
  </section>
</main>
</body>
</html>
```